Corwin Tably Interiors
business card and stationary
Corwin Tably Interiors -
Creative Brief
Simple
corwin tably
interior designer
studio: 27 brookfen lane pacifica, california 94044
corwin@corwintablyinteriors.example
http://corwintablyinteriors.example
the graphic part of my logo is something i will use a lot in my branding. i like the idea of repitition or a very large version of it in a single color or grayscale that bleeds off the card.
i like the grayscale logo (white burst) on the gray background a lot. i want one side of the card to be white background, probably the front.

```html
<!DOCTYPE html>
<html lang="en">
<head>
<meta charset="utf-8">
<title>Corwin Tably Interiors — Business Card</title>
<link href="https://fonts.googleapis.com/css2?family=Raleway:wght@300;400;500&display=swap" rel="stylesheet">
<style>
  :root {
    --page: #ecebe8;
    --card-white: #ffffff;
    --card-gray: #8a8d92;
    --ink: #6d7075;
    --accent: #5fb3d3;
    --accent-deep: #3f95b8;
    --leaf: #b7cf8a;
    --mark-back: #c9ccd0;
    --name-back: #f4f5f6;
    --burst-tint: #eef4f1;
  }
  * { margin: 0; padding: 0; box-sizing: border-box; }
  html, body { width: 1200px; height: 646px; overflow: hidden; }
  body {
    background: var(--page);
    font-family: "Raleway", Arial, sans-serif;
    position: relative;
  }
  .card {
    position: absolute;
    top: 174px;
    width: 520px;
    height: 298px;
    overflow: hidden;
    box-shadow: 0 2px 8px rgba(0,0,0,0.12);
  }
  .card--front { left: 60px; background: var(--card-white); }
  .card--back { left: 620px; background: var(--card-gray); }

  /* large faint brand wash bleeding off the right edge */
  .brand-wash {
    position: absolute;
    right: -70px;
    top: -40px;
    width: 330px;
    height: 330px;
    border-radius: 50%;
    background: radial-gradient(circle, var(--burst-tint) 0%, #f5f9f7 55%, rgba(255,255,255,0) 72%);
  }

  .wordmark {
    position: absolute;
    display: flex;
    flex-direction: column;
  }
  .wordmark__dot {
    width: 38px; height: 38px; border-radius: 50%;
    background: var(--leaf);
    flex: none;
  }
  .wordmark__name {
    font-weight: 300;
    line-height: 1.05;
    text-transform: lowercase;
  }
  .card--front .wordmark { left: 30px; top: 52px; gap: 8px; align-items: flex-start; }
  .card--front .wordmark__name { color: var(--ink); font-size: 30px; }
  .card--front .wordmark__name span { display: block; font-size: 13px; letter-spacing: 7px; margin-top: 4px; }

  .card--back .wordmark { left: 50%; top: 50%; transform: translate(-50%, -50%); align-items: center; gap: 10px; text-align: center; white-space: nowrap; }
  .card--back .wordmark__dot { width: 56px; height: 56px; background: var(--mark-back); }
  .card--back .wordmark__name { color: var(--name-back); font-size: 22px; letter-spacing: 1px; }

  .title-tab {
    position: absolute;
    right: 0;
    top: 70px;
    display: flex;
    align-items: stretch;
  }
  .title-tab__text { text-align: right; padding-right: 8px; }
  .title-tab__name { color: var(--accent-deep); font-size: 15px; font-weight: 400; }
  .title-tab__role { color: var(--accent); font-size: 10px; font-weight: 400; margin-top: 2px; }
  .title-tab__bar { width: 16px; background: var(--accent); }

  .contact {
    position: absolute;
    left: 30px;
    bottom: 20px;
    list-style: none;
    color: var(--ink);
    font-size: 10.5px;
    font-weight: 400;
  }
  .contact li { display: flex; align-items: center; gap: 7px; margin-top: 5px; }
  .contact li.address { display: block; line-height: 1.35; margin-bottom: 3px; }
  .contact svg { width: 11px; height: 11px; flex: none; }
</style>
</head>
<body>

  <section class="card card--front" aria-label="Business card front">
    <div class="brand-wash" role="img" aria-label="Large faint brand mark bleeding off the card edge"></div>

    <div class="wordmark">
      <div class="wordmark__dot"></div>
      <div class="wordmark__name">corwin tably<span>interiors</span></div>
    </div>

    <div class="title-tab">
      <div class="title-tab__text">
        <div class="title-tab__name">corwin tably</div>
        <div class="title-tab__role">interior designer</div>
      </div>
      <div class="title-tab__bar"></div>
    </div>

    <ul class="contact">
      <li class="address">studio: 27 brookfen lane<br>marlow bay, california 94190</li>
      <li>
        <svg viewBox="0 0 12 12"><circle cx="6" cy="6" r="6" fill="var(--accent)"/><path d="M4 3.2h1.2l.6 1.6-.8.6a4 4 0 0 0 1.6 1.6l.6-.8 1.6.6V8A1 1 0 0 1 7.6 9 5 5 0 0 1 3 4.4 1 1 0 0 1 4 3.2z" fill="#fff"/></svg>
        415.555.0172
      </li>
      <li>
        <svg viewBox="0 0 12 12"><circle cx="6" cy="6" r="6" fill="var(--accent)"/><rect x="3" y="4" width="6" height="4.2" fill="none" stroke="#fff" stroke-width=".9"/><path d="M3 4l3 2.3L9 4" fill="none" stroke="#fff" stroke-width=".9"/></svg>
        corwin@corwintablyinteriors.example
      </li>
      <li>
        <svg viewBox="0 0 12 12"><circle cx="6" cy="6" r="6" fill="var(--accent)"/><circle cx="6" cy="6" r="3" fill="none" stroke="#fff" stroke-width=".8"/><path d="M3 6h6M6 3c-1.4 1.6-1.4 4.4 0 6M6 3c1.4 1.6 1.4 4.4 0 6" fill="none" stroke="#fff" stroke-width=".7"/></svg>
        http://corwintablyinteriors.example
      </li>
      <li>
        <svg viewBox="0 0 12 12"><circle cx="6" cy="6" r="6" fill="var(--accent)"/><path d="M3.2 4.2h5.6v3.2H5.4L4 8.8V7.4h-.8z" fill="#fff"/></svg>
        ctably
      </li>
    </ul>
  </section>

  <section class="card card--back" aria-label="Business card back">
    <div class="wordmark">
      <div class="wordmark__dot"></div>
      <div class="wordmark__name">corwin tably interiors</div>
    </div>
  </section>

</body>
</html>
```